Tr construction holdings pty ltd

2 sided card black and red with white
Very professional and elegant

Target Market(s)

Construction and Development

Industry/Entity Type

Construction and development

Contact Information for Business Card

One side black, one side red/or white business logo in top corner, email: morgan@trbuildworks.example

Requirements
Should not have
• Blue

```html
<!DOCTYPE html>
<html lang="en">
<head>
<meta charset="utf-8">
<title>TR Construction – Business Card</title>
<link href="https://fonts.googleapis.com/css2?family=Montserrat:wght@600&family=Open+Sans:wght@400&display=swap" rel="stylesheet">
<style>
  :root {
    --page: #f4f5f7;
    --ink-black: #070909;
    --brand-red: #e5392a;
    --paper-white: #ffffff;
    --text-dark: #1d1d1f;
    --decor-dark-a: #343232;
    --decor-dark-b: #1c1a1a;
    --decor-light-a: #e2e3e5;
    --decor-light-b: #c9c9cb;
  }
  * { margin: 0; padding: 0; box-sizing: border-box; }
  html, body {
    width: 1200px; height: 441px; overflow: hidden;
    background: var(--page);
  }
  .canvas { position: relative; width: 1200px; height: 441px; }
  .card {
    position: absolute; top: 96px;
    width: 436px; height: 249px; overflow: hidden;
  }
  .card--front { left: 96px; background: var(--ink-black); }
  .card--back  { left: 649px; background: var(--paper-white); }

  .front-decor {
    position: absolute; left: 277px; top: 36px;
    width: 180px; height: 178px;
    border-radius: 89px 0 0 89px;
    background: linear-gradient(90deg, var(--decor-dark-a), var(--decor-dark-b));
    opacity: .8;
  }
  .brand-name {
    font-family: "Montserrat", sans-serif; font-weight: 600;
    letter-spacing: .04em; white-space: nowrap;
    display: flex; align-items: baseline; gap: 3px;
  }
  .brand-dot {
    display: inline-block; border-radius: 50%; background: var(--brand-red);
  }
  .card--front .brand-name {
    position: absolute; left: 0; right: 0; top: 100px;
    justify-content: center;
    font-size: 25px; color: var(--paper-white);
  }
  .card--front .brand-dot { width: 6px; height: 6px; }

  .back-decor {
    position: absolute; left: 0; top: 36px;
    width: 163px; height: 178px;
    border-radius: 0 70px 70px 0;
    background: linear-gradient(90deg, var(--decor-light-a), var(--decor-light-b));
    opacity: .85;
  }
  .card--back .brand-name {
    position: absolute; right: 15px; top: 48px;
    font-size: 14px; color: var(--text-dark);
  }
  .card--back .brand-dot { width: 4px; height: 4px; }
  .brand-rule {
    position: absolute; left: 285px; right: 0; top: 80px;
    height: 3px; background: var(--brand-red);
  }
  .contact {
    position: absolute; left: 0; top: 219px;
    display: flex; align-items: center; gap: 11px;
  }
  .contact-marker { width: 7px; height: 14px; background: var(--brand-red); }
  .contact-email {
    font-family: "Open Sans", sans-serif; font-size: 15.5px;
    color: var(--text-dark); line-height: 1;
  }
</style>
</head>
<body>
<main class="canvas">
  <section class="card card--front" aria-label="Card front">
    <div class="front-decor" aria-hidden="true"></div>
    <p class="brand-name">TR CONSTRUCTION<span class="brand-dot"></span></p>
  </section>

  <section class="card card--back" aria-label="Card back">
    <div class="back-decor" aria-hidden="true"></div>
    <p class="brand-name">TR CONSTRUCTION<span class="brand-dot"></span></p>
    <div class="brand-rule"></div>
    <div class="contact">
      <span class="contact-marker"></span>
      <span class="contact-email">morgan@trbuildworks.example</span>
    </div>
  </section>
</main>
</body>
</html>
```